Wordpress Design Project for lorettabramwell.com.au

PLEASE NOTE ...Coding Required

I need a simple website to display my art. There will be 4 different categories - FloraGrandis (botanical art), Oceanlife, Travel Sketchbook, Portraits. There needs to be room for an introduction to me and my work,photos of my studio and views from here and a description of each individual piece. I will probably display no more than 10 pieces in category. Obviously I need to change photos on a regular basis.

I would also like to include a Coinvale button to be connected to my Coinvale account.

I have already started to do a website on Wordpress but am finding it too hard to do.

Thank you

Doreen

Reason: I have provided a deadline extension as I feel the initial lead up time could be too short. Hope that helps you. Doreen

Dear designers. Thankyou all so much for submitting some beautiful designs. I will spend time this weekend evaluating them but as the closing date is January 19, I will not make final decisions until then.  You have probably received an update by now butI  just want to mention that Coding is required.

Cheers

Doreen

Thank you Designers for your patience.  I have been advised by PixelHarbor that I cannot make a decision until the deadline has passed, so will let you know on Saturday.

Thank you.
Doreen.

Target Market(s)

35 to 75 who want to buy art and very personal gifts

Industry/Entity Type

Travel

Requirements
Must have
• Ability to change photos often. Modern, elegant, streamlined
Nice to have
• The colour green, an elegant font - sans serif and definitely not courier; room for a photo of me (maybe), and an interesting headline font
Should not have
• quirky, cartooney, retro.

```html
<!DOCTYPE html>
<html lang="en">
<head>
<meta charset="utf-8">
<title>Doreen Ann Bramwell — Art</title>
<link rel="stylesheet" href="https://fonts.googleapis.com/css2?family=Great+Vibes&family=Lato:wght@700&display=swap">
<style>
  :root {
    --sky: #d3e5e8;
    --meadow: #e6eec4;
    --meadow-deep: #dfe9b4;
    --frame: #b8c5ab;
    --frame-edge: #a9b89b;
    --ink: #6d6a66;
    --ink-dark: #4f4c48;
    --arrow: #8c6a4a;
    --tab: #fbf7dc;
    --bar: #e7efc6;
    --icon: #8f9a8c;
  }
  * { margin: 0; padding: 0; box-sizing: border-box; }
  html, body { width: 1200px; height: 747px; overflow: hidden; }
  body {
    position: relative;
    background: linear-gradient(180deg, var(--sky) 0%, var(--meadow) 45%, var(--meadow-deep) 100%);
    font-family: "Great Vibes", cursive;
    color: var(--ink);
  }
  .social-tab {
    position: absolute; left: 842px; top: 0; width: 162px; height: 42px;
    background: var(--tab);
    box-shadow: 0 2px 4px rgba(0,0,0,.12);
    display: flex; align-items: center; justify-content: center; gap: 6px;
  }
  .social-link {
    font-family: "Lato", sans-serif; font-weight: 700; font-size: 9px;
    color: var(--icon); text-decoration: none;
  }
  .site-title {
    position: absolute; left: 0; top: 60px; width: 1230px; text-align: center;
    font-size: 58px; font-weight: 400; color: #77726c;
    text-shadow: 1px 1px 0 #fff, 2px 3px 3px rgba(0,0,0,.25);
  }
  .nav-arrow { position: absolute; top: 283px; width: 28px; height: 110px; }
  .nav-arrow.prev { left: 114px; }
  .nav-arrow.next { left: 1068px; }
  .gallery-card { position: absolute; top: 187px; width: 244px; }
  .card-frame {
    width: 244px; height: 321px; padding: 18px 22px;
    background: var(--frame); border-radius: 24px;
    box-shadow: inset 0 0 0 2px var(--frame-edge), 0 4px 8px rgba(0,0,0,.18);
  }
  .card-art { width: 200px; height: 282px; border-radius: 16px; }
  .art-flora { background: radial-gradient(circle at 45% 30%, #f08a6e 0%, #f3b7a3 30%, #f4f2ee 60%); }
  .art-ocean { background: radial-gradient(circle at 45% 45%, #3f7a3c 0%, #8fb184 35%, #f2f2ee 70%); }
  .art-travel { background: linear-gradient(135deg, #c9dbb3 0%, #eef1e4 50%, #b7cf98 100%); }
  .card-caption {
    margin-top: 12px; text-align: center; font-size: 27px; color: var(--ink-dark);
    text-shadow: 1px 1px 0 #fff, 1px 2px 2px rgba(0,0,0,.2);
  }
  .main-nav {
    position: absolute; left: 0; top: 703px; width: 1200px; height: 44px;
    background: var(--bar); box-shadow: 0 -3px 5px rgba(0,0,0,.15);
  }
  .main-nav a {
    position: absolute; top: 6px; transform: translateX(-50%);
    font-size: 27px; color: var(--ink-dark); text-decoration: none; white-space: nowrap;
    text-shadow: 1px 1px 0 #fff, 1px 2px 2px rgba(0,0,0,.25);
  }
</style>
</head>
<body>
  <div class="social-tab">
    <a class="social-link" href="#">Linkle</a>
    <a class="social-link" href="#">Chirpa</a>
    <a class="social-link" href="#">Pinnery</a>
    <a class="social-link" href="#">Circlo</a>
  </div>

  <h1 class="site-title">Doreen Ann Bramwell</h1>

  <svg class="nav-arrow prev" viewBox="0 0 28 110" aria-label="Previous">
    <path d="M26 2 L3 55 L26 108" fill="none" stroke="var(--arrow)" stroke-width="5" stroke-linecap="round" stroke-linejoin="round"/>
  </svg>
  <svg class="nav-arrow next" viewBox="0 0 28 110" aria-label="Next">
    <path d="M2 2 L25 55 L2 108" fill="none" stroke="var(--arrow)" stroke-width="5" stroke-linecap="round" stroke-linejoin="round"/>
  </svg>

  <div class="gallery-card" style="left:200px">
    <div class="card-frame"><div class="card-art art-flora" role="img" aria-label="Watercolour of a large coral flower with blossoms on a branch"></div></div>
    <p class="card-caption">FloraGrandis</p>
  </div>
  <div class="gallery-card" style="left:480px">
    <div class="card-frame"><div class="card-art art-ocean" role="img" aria-label="Botanical painting of green leaves with pink frangipani flowers"></div></div>
    <p class="card-caption">Oceanlife</p>
  </div>
  <div class="gallery-card" style="left:761px">
    <div class="card-frame"><div class="card-art art-travel" role="img" aria-label="Sketch of daisies over a loose green watercolour wash"></div></div>
    <p class="card-caption">Travel Sketchbook</p>
  </div>

  <nav class="main-nav">
    <a href="#" style="left:316px">Home</a>
    <a href="#" style="left:439px">About Me</a>
    <a href="#" style="left:586px">My Work</a>
    <a href="#" style="left:727px">My Studio</a>
    <a href="#" style="left:874px">Lets Talk</a>
  </nav>
</body>
</html>
```